Need webdesign for service company that provides Car hiring service and transit service

We need a web design for a company that provides airport transit services and transport services including Limo, Corporate cars, Disability transit, Family transit service. We need is a simple and professional design.

Below is site which we like and also offer the same service http://www.ridevelto.com.au/

Reason: Waiting for the Feedback from multiple stakeholders. Need the time to select and approve the design

Target Market(s)

Tourism, Travel

Industry/Entity Type

Airport

Number of Pages Required

3 page

Font styles to use
Decorative
Script

Requirements
Must have
• Simple and Professional, Site we like http://www.ridevelto.com.au/ and also need to mobile friendly
Should not have
• Shouldn't have too many images

```html
<!DOCTYPE html>
<html lang="en">
<head>
<meta charset="utf-8">
<title>Rovano — Private &amp; Business Transport</title>
<link rel="stylesheet" href="https://fonts.googleapis.com/css2?family=Lato:wght@400;700;900&family=Libre+Caslon+Text:wght@700&family=Open+Sans:wght@300;400;700&display=swap">
<style>
  :root{
    --ink:#111111;
    --black:#000000;
    --white:#ffffff;
    --grey-text:#666666;
    --brand-grey:#333333;
    --panel:#e6e6e6;
    --button:#736e70;
    --field-border:#d6d6d6;
  }
  *{margin:0;padding:0;box-sizing:border-box;}
  html,body{width:1060px;height:1200px;overflow:hidden;background:var(--white);}
  body{position:relative;font-family:"Lato",sans-serif;color:var(--ink);}

  .top-strip{position:absolute;left:0;top:0;width:1060px;height:5px;background:var(--black);}
  .site-header{position:absolute;left:0;top:5px;width:1060px;height:108px;background:var(--white);}
  .header-shadow{position:absolute;left:0;top:113px;width:1060px;height:10px;
    background:linear-gradient(90deg,rgba(0,0,0,.35),rgba(0,0,0,.12) 40%,rgba(0,0,0,0) 45%,rgba(0,0,0,0) 57%,rgba(0,0,0,.12) 62%,rgba(0,0,0,.35));
    -webkit-mask:linear-gradient(#000,transparent);mask:linear-gradient(#000,transparent);}

  .brand{position:absolute;left:90px;top:34px;display:flex;align-items:center;gap:12px;}
  .brand-square{width:14px;height:14px;background:var(--brand-grey);}
  .brand-name{font-size:34px;font-weight:400;letter-spacing:1px;line-height:1;color:var(--brand-grey);}
  .brand-tagline{font-size:9px;font-weight:700;letter-spacing:.4px;color:#555;margin-top:4px;}

  .header-tools{position:absolute;top:34px;right:88px;display:flex;align-items:center;}
  .diamond-btn{width:45px;height:45px;}
  .phone-number{font-size:17px;font-weight:700;margin:0 30px 0 10px;}
  .header-tools .diamond-btn + .diamond-btn{margin-left:8px;}

  .tagline-block{position:absolute;left:0;top:145px;width:1060px;text-align:center;}
  .tagline-title{font-family:"Libre Caslon Text",serif;font-size:29px;font-weight:700;display:inline-block;
    padding:0 22px 2px;border-bottom:1px solid #444;line-height:1.1;}
  .tagline-title .amp{font-size:34px;}
  .tagline-sub{font-size:18px;color:var(--grey-text);letter-spacing:.3px;margin-top:1px;}

  .hero{position:absolute;left:0;top:235px;width:1060px;height:488px;
    background:linear-gradient(180deg,#c6d8e6 0%,#e3e9ee 30%,#c9c7c4 62%,#8f9296 80%,#6e7276 100%);}

  .quote-box{position:absolute;left:87px;top:335px;width:310px;height:288px;background:var(--black);padding:0 18px;}
  .quote-title{color:var(--white);font-size:22px;font-weight:700;text-align:center;margin:19px 0 15px;}
  .quote-field{display:flex;align-items:center;background:var(--white);height:34px;margin-bottom:11px;font-size:11px;}
  .quote-field .field-icon{width:29px;height:100%;display:flex;align-items:center;justify-content:center;border-right:1px solid var(--field-border);}
  .quote-field .field-label{padding-left:11px;}
  .quote-field.tall{height:53px;margin-bottom:21px;}
  .quote-field.tall .field-label{line-height:21px;}
  .add-stop{display:flex;align-items:center;gap:8px;}
  .add-stop .plus{width:14px;height:14px;border:1px solid #bbb;font-size:12px;line-height:12px;text-align:center;font-weight:700;}
  .estimate-btn{display:block;width:100%;height:37px;background:var(--button);color:var(--white);border:0;
    font-family:"Lato",sans-serif;font-size:18px;font-weight:700;letter-spacing:.3px;}

  .about{position:absolute;left:89px;top:776px;width:440px;}
  .about h2{font-family:"Open Sans",sans-serif;font-weight:400;font-size:26px;letter-spacing:.3px;margin-bottom:12px;}
  .about h2 strong{font-weight:700;}
  .about p{font-size:11.6px;line-height:23px;letter-spacing:.15px;margin-bottom:8px;}

  .services{position:absolute;left:555px;top:762px;width:418px;height:357px;background:var(--panel);}
  .service{position:absolute;width:210px;text-align:center;}
  .service svg{width:98px;height:98px;display:block;margin:0 auto;}
  .service-name{font-size:15px;font-weight:700;margin-top:19px;letter-spacing:.1px;}
  .s1{left:-5px;top:27px;} .s2{left:194px;top:27px;}
  .s3{left:-5px;top:201px;} .s4{left:194px;top:201px;}

  .site-footer{position:absolute;left:0;top:1159px;width:1060px;height:41px;background:var(--black);color:var(--white);}
  .copyright{position:absolute;left:89px;top:13px;font-size:12px;}
  .social{position:absolute;right:85px;top:8px;display:flex;gap:5px;}
  .social svg{width:26px;height:26px;}
</style>
</head>
<body>
  <div class="top-strip"></div>
  <header class="site-header">
    <div class="brand">
      <span class="brand-square" aria-hidden="true"></span>
      <div>
        <div class="brand-name">ROVANO</div>
        <div class="brand-tagline">RIDES ARRANGED WITH CARE</div>
      </div>
    </div>
    <div class="header-tools">
      <svg class="diamond-btn" viewBox="0 0 45 45" aria-label="Call"><rect x="9" y="9" width="27" height="27" transform="rotate(45 22.5 22.5)" fill="none" stroke="#111" stroke-width="1.5"/><path d="M16 15c1-1 2-1 3 0l2 3c.6 1 .3 1.7-.5 2.4l-.8.7c.8 2 2.2 3.5 4.2 4.4l.8-.8c.7-.7 1.5-1 2.4-.4l3 2c1 .8 1 1.8 0 2.8l-1.2 1.2c-1.5 1.5-5 .4-8.6-3.2S14.3 18.8 15.6 16.8z" fill="#111"/></svg>
      <span class="phone-number">123 456 7890</span>
      <svg class="diamond-btn" viewBox="0 0 45 45" aria-label="Menu"><rect x="9" y="9" width="27" height="27" transform="rotate(45 22.5 22.5)" fill="none" stroke="#111" stroke-width="1.5"/><g stroke="#111" stroke-width="2.4" stroke-linecap="round"><path d="M15 17.5h15M15 22.5h15M15 27.5h15"/></g></svg>
      <svg class="diamond-btn" viewBox="0 0 45 45" aria-label="Search"><rect x="9" y="9" width="27" height="27" transform="rotate(45 22.5 22.5)" fill="none" stroke="#111" stroke-width="1.5"/><circle cx="21" cy="21" r="5.5" fill="none" stroke="#111" stroke-width="2.2"/><path d="M25 25l4.5 4.5" stroke="#111" stroke-width="2.4" stroke-linecap="round"/></svg>
    </div>
  </header>
  <div class="header-shadow"></div>

  <section class="tagline-block">
    <div class="tagline-title">Private <span class="amp">&amp;</span> Business</div>
    <div class="tagline-sub">Personalised Transport Services</div>
  </section>

  <section class="hero" role="img" aria-label="Photo of a silver limousine parked beside a private jet on the tarmac, with travellers greeted by crew"></section>

  <form class="quote-box">
    <h2 class="quote-title">GET INSTANT QUOTE</h2>
    <div class="quote-field"><span class="field-icon"><svg width="11" height="11" viewBox="0 0 11 11"><circle cx="5.5" cy="5.5" r="4.5" fill="none" stroke="#111" stroke-width="1.2"/></svg></span><span class="field-label">Origin ( Public Location Or Exact Address )</span></div>
    <div class="quote-field"><span class="field-icon"><svg width="10" height="14" viewBox="0 0 10 14"><path d="M5 0a5 5 0 0 1 5 5c0 3.5-5 9-5 9S0 8.5 0 5a5 5 0 0 1 5-5z" fill="#111"/><circle cx="5" cy="5" r="1.8" fill="#fff"/></svg></span><span class="field-label">Destination ( Public Location Or Exact Address )</span></div>
    <div class="quote-field tall"><span class="field-icon"><svg width="11" height="11" viewBox="0 0 11 11"><circle cx="5.5" cy="5.5" r="4.5" fill="none" stroke="#111" stroke-width="1.2"/></svg></span>
      <div class="field-label"><div>Show other vehicles</div><div class="add-stop"><span class="plus">+</span>Add Stops</div></div></div>
    <button type="button" class="estimate-btn">ESTIMATE FARE</button>
  </form>

  <section class="about">
    <h2>ABOUT <strong>US</strong></h2>
    <p>Fusce a lorem felis. Nulla quis tellus vulputate, pellentesque tortor in, dictum ligula. Ut pretium sem elit, quis luctus eros blandit sed. Mauris nec lacus elementum, vulputate orci sed, ullamcorper nulla. Etiam tempor lorem quis metus imperdiet aliquet. Vestibulum at mi risus. Sed mattis maximus tristique. Vivamus sollicitudin tellus sed velit accumsan, sed iaculis ligula dignissim. Maecenas accumsan ut dui vel commodo. Integer varius tortor at ipsum efficitur lobortis. Ut posuere in dui nec bibendum lectus bibendum est iaculis dignissim.</p>
    <p>Fusce a lorem felis. Nulla quis tellus vulputate, pellentesque tortor in, dictum ligula. Ut pretium sem elit, quis luctus eros blandit sed. Mauris nec lacus elementum, vulputate orci sed, ullamcorper nulla. Etiam tempor lorem quis metus imperdiet aliquet. Vestibulum at mi risus. Sed mattis maximus tristique. Vivamus sollicitudin tellus sed velit accumsan, sed iaculis ligula dignissim.</p>
  </section>

  <section class="services">
    <div class="service s1">
      <svg viewBox="0 0 98 98" aria-hidden="true"><rect x="20" y="20" width="58" height="58" transform="rotate(45 49 49)" fill="#fff" stroke="#000" stroke-width="3.5"/><path d="M25 56v-6c0-2 1-3 3-3.5l8-1.5 6-5h14l7 5 7 1c2 .5 3 1.5 3 3.5v7z" fill="#111"/><path d="M43 41.5h6v4h-10zM51 41.5h4l5 4h-9z" fill="#fff"/><circle cx="35" cy="56" r="4.5" fill="#111" stroke="#fff" stroke-width="1.5"/><circle cx="63" cy="56" r="4.5" fill="#111" stroke="#fff" stroke-width="1.5"/></svg>
      <div class="service-name">CORPORATE CARS</div>
    </div>
    <div class="service s2">
      <svg viewBox="0 0 98 98" aria-hidden="true"><rect x="20" y="20" width="58" height="58" transform="rotate(45 49 49)" fill="#fff" stroke="#000" stroke-width="3.5"/><path d="M35 44l3-6h22l3 6h2v14H33V44z" fill="#111"/><path d="M39.5 43l2-3.5h15l2 3.5z" fill="#fff"/><rect x="43" y="47" width="12" height="7" fill="#fff"/><path d="M45 47v7M47.5 47v7M50 47v7M52.5 47v7" stroke="#111"/><rect x="35" y="58" width="5" height="4" fill="#111"/><rect x="58" y="58" width="5" height="4" fill="#111"/></svg>
      <div class="service-name">LIMO SERVICE</div>
    </div>
    <div class="service s3">
      <svg viewBox="0 0 98 98" aria-hidden="true"><rect x="20" y="20" width="58" height="58" transform="rotate(45 49 49)" fill="#fff" stroke="#000" stroke-width="3.5"/><circle cx="45" cy="36" r="3.2" fill="#111"/><path d="M44 41v11h10l4 8" fill="none" stroke="#111" stroke-width="3.5" stroke-linecap="round" stroke-linejoin="round"/><path d="M44 46h7" stroke="#111" stroke-width="3" stroke-linecap="round"/><path d="M40 47a9 9 0 1 0 13 10" fill="none" stroke="#111" stroke-width="2.8"/></svg>
      <div class="service-name">DISABILITY TRANSIT</div>
    </div>
    <div class="service s4">
      <svg viewBox="0 0 98 98" aria-hidden="true"><rect x="20" y="20" width="58" height="58" transform="rotate(45 49 49)" fill="#fff" stroke="#000" stroke-width="3.5"/><rect x="33" y="37" width="23" height="22" rx="3" fill="#111"/><rect x="36" y="41" width="17" height="7" fill="#fff"/><circle cx="38" cy="53" r="1.5" fill="#fff"/><circle cx="51" cy="53" r="1.5" fill="#fff"/><rect x="35" y="59" width="4" height="3" fill="#111"/><rect x="50" y="59" width="4" height="3" fill="#111"/><circle cx="60" cy="47" r="1.5" fill="#111"/><rect x="58.5" y="49.5" width="3" height="8" fill="#111"/><circle cx="65.5" cy="47" r="1.5" fill="#111"/><rect x="64" y="49.5" width="3" height="8" fill="#111"/><circle cx="62.8" cy="52" r="1" fill="#111"/><rect x="62" y="53.5" width="1.8" height="4" fill="#111"/></svg>
      <div class="service-name">FAMILY TRANSIT SERVICE</div>
    </div>
  </section>

  <footer class="site-footer">
    <div class="copyright">Copyright © 2017 ROVANO. All Rights Reserved.</div>
    <div class="social" aria-label="Social links">
      <svg viewBox="0 0 26 26" aria-hidden="true"><rect x="5" y="5" width="16" height="16" transform="rotate(45 13 13)" fill="none" stroke="#fff" stroke-width="1.2"/><circle cx="13" cy="13" r="2.5" fill="#fff"/></svg>
      <svg viewBox="0 0 26 26" aria-hidden="true"><rect x="5" y="5" width="16" height="16" transform="rotate(45 13 13)" fill="none" stroke="#fff" stroke-width="1.2"/><circle cx="13" cy="13" r="2.5" fill="#fff"/></svg>
      <svg viewBox="0 0 26 26" aria-hidden="true"><rect x="5" y="5" width="16" height="16" transform="rotate(45 13 13)" fill="none" stroke="#fff" stroke-width="1.2"/><circle cx="13" cy="13" r="2.5" fill="#fff"/></svg>
    </div>
  </footer>
</body>
</html>
```